Business Card Re-Design for a Lighting Designer

I would like my business card re-designed. It is currently high gloss and they scratch too easily. I don not think the current design lends itself well to a matte finish. I have included the current design for reference along with our company logo.
Check out our website for current branding.
http://www.brambleorchidstudio.example

Updates
Some of the top contenders are muslim and it is a holiday for them. I do not want to discriminate and would expect the same courtesy for holidays we celebrate.
Target Market(s)
Interior Designers, Architects
Contact Information for Business Card
Logo - Name, Title, Address, Telephone Number and Extension, Email
Font styles to use
Requirements
Must have
- All the information listed on the current business card. If you use Red, it needs to be the red from our logo.
Nice to have
- Vertical and Horizontal Designs will be entertained.
Should not have
- Requirements for a glossy finish...should not look too corporate since we are a design firm.

```html
<!DOCTYPE html>
<html lang="en">
<head>
<meta charset="utf-8">
<title>Bramble Orchid Studio — Business Card</title>
<link rel="stylesheet" href="https://fonts.googleapis.com/css2?family=Maven+Pro:wght@400;500&display=swap">
<style>
  :root {
    --backdrop: #3a3a3a;
    --brand-red: #9b1b1f;
    --brand-red-light: #b62228;
    --card-white: #ffffff;
    --ink: #3b3b3b;
    --ink-soft: #555555;
  }
  * { box-sizing: border-box; margin: 0; padding: 0; }
  html, body { width: 1200px; height: 900px; overflow: hidden; }
  body {
    background: var(--backdrop);
    font-family: "Maven Pro", sans-serif;
    color: var(--ink);
    display: flex;
    flex-direction: column;
    align-items: center;
    justify-content: center;
    gap: 40px;
  }
  .card {
    width: 700px;
    height: 400px;
    position: relative;
    box-shadow: 0 6px 18px rgba(0,0,0,.35);
  }
  /* Card back */
  .card--back {
    background: var(--brand-red);
    display: flex;
    align-items: center;
    justify-content: center;
  }
  .back-wordmark {
    display: flex;
    align-items: center;
    gap: 22px;
    color: var(--brand-red-light);
    font-weight: 500;
    font-size: 40px;
    letter-spacing: 1px;
    text-transform: uppercase;
  }
  .back-wordmark__square {
    width: 110px;
    height: 110px;
    background: var(--brand-red-light);
  }
  /* Card front */
  .card--front { background: var(--card-white); }
  .front-wordmark {
    position: absolute;
    left: 44px;
    top: 40px;
    display: flex;
    align-items: center;
    gap: 14px;
    color: var(--brand-red);
    font-weight: 500;
    font-size: 24px;
    text-transform: uppercase;
    letter-spacing: .5px;
  }
  .front-wordmark__square {
    width: 58px;
    height: 58px;
    background: var(--brand-red);
  }
  .divider {
    position: absolute;
    left: 44px;
    right: 44px;
    top: 232px;
    height: 1.5px;
    background: var(--brand-red);
  }
  .contact {
    position: absolute;
    left: 44px;
    top: 262px;
    font-size: 19px;
    line-height: 1.45;
    color: var(--ink);
  }
  .person {
    position: absolute;
    right: 44px;
    top: 246px;
    text-align: right;
  }
  .person__name {
    color: var(--brand-red);
    font-size: 21px;
    font-weight: 500;
    letter-spacing: 1px;
    text-transform: uppercase;
  }
  .person__title {
    font-size: 18px;
    color: var(--ink-soft);
  }
  .address {
    position: absolute;
    right: 44px;
    top: 316px;
    text-align: right;
    font-size: 18px;
    line-height: 1.45;
    font-style: normal;
    color: var(--ink);
  }
</style>
</head>
<body>
  <section class="card card--back" aria-label="Card back">
    <div class="back-wordmark">
      <span class="back-wordmark__square"></span>
      <span class="back-wordmark__name">Bramble Orchid Studio</span>
    </div>
  </section>

  <section class="card card--front" aria-label="Card front">
    <div class="front-wordmark">
      <span class="front-wordmark__square"></span>
      <span class="front-wordmark__name">Bramble Orchid Studio</span>
    </div>
    <div class="divider"></div>
    <div class="contact">
      <div class="contact__phone">555 014 2290 X1</div>
      <div class="contact__email">maren@brambleorchidstudio.example</div>
      <div class="contact__web">www.brambleorchidstudio.example</div>
    </div>
    <div class="person">
      <div class="person__name">Maren Oakley</div>
      <div class="person__title">Principal</div>
    </div>
    <address class="address">
      210 Larkspur Row<br>
      Suite 40, Dunmore<br>
      Ohio 45001 USA
    </address>
  </section>
</body>
</html>
```